Hiring Infographic

We need an infographic for displaying on a website and sharing via social media. Attached is an example of a prior infographic developed for the client for reference (Orchard Ledger). The data for the new infographic is in the attached Mocrosoft Word document about hiring.

Media

```html
<!DOCTYPE html>
<html lang="en">
<head>
<meta charset="utf-8">
<title>Hiring the Right People</title>
<link rel="stylesheet" href="https://fonts.googleapis.com/css2?family=Oswald:wght@400;500;700&family=Open+Sans:wght@400;600;700&display=swap">
<style>
:root{
  --teal:#3c8a8b;
  --teal-dark:#2f6f70;
  --teal-light:#8fc2c2;
  --orange:#e8663a;
  --orange-soft:#f08a63;
  --cream:#f4eedd;
  --ink:#444444;
  --gray:#9a9a9a;
  --white:#ffffff;
}
*{box-sizing:border-box;margin:0;padding:0}
html,body{width:1200px;height:4319px;overflow:hidden}
body{background:var(--cream);font-family:"Open Sans",Arial,sans-serif;color:var(--ink);position:relative}
.abs{position:absolute}
.heading{font-family:"Oswald",Arial,sans-serif;text-transform:uppercase;font-weight:700;text-align:center}

/* header */
.masthead{top:0;left:0;width:1200px;height:110px;background:var(--teal);text-align:center;padding-top:6px}
.masthead h1{font-family:"Oswald",Arial,sans-serif;color:var(--orange);font-size:56px;line-height:58px;letter-spacing:2px}
.masthead h2{font-family:"Oswald",Arial,sans-serif;color:var(--white);font-size:30px;line-height:38px;font-weight:500;letter-spacing:2px}
.team-figures{top:118px;left:380px;width:440px;height:162px;background:linear-gradient(#5a5a5a,#3a3a3a);border-radius:110px 110px 0 0}
.intro{top:280px;left:90px;width:1020px;height:262px;background:var(--orange);color:var(--white);padding:18px 40px;font-size:15px;line-height:1.45}
.intro p+p{margin-top:8px}

/* three forces */
.forces-title{top:565px;left:0;width:1200px;font-size:46px;line-height:54px}
.force{top:690px;width:300px;text-align:center}
.pin{width:166px;height:166px;margin:0 auto;border-radius:50%;background:var(--gray);display:flex;align-items:center;justify-content:center}
.pin span{width:122px;height:122px;border-radius:50%;background:var(--white);font-family:"Oswald",Arial,sans-serif;font-size:84px;line-height:122px;color:var(--ink)}
.pin-tip{display:block;margin:-8px auto 0}
.force-box{background:var(--teal);color:var(--white);height:330px;margin-top:4px;padding:16px 20px}
.force-box h3{font-family:"Oswald",Arial,sans-serif;font-size:26px;line-height:32px;margin-bottom:8px}
.force-box p{font-size:14.5px;line-height:1.45}

/* qualities */
.qualities-title{top:1245px;left:90px;width:1020px;font-size:34px;line-height:44px;color:var(--orange);text-align:left;font-weight:500}
.qualities-title b{color:var(--ink);font-weight:500}
.quality{left:90px;width:1020px;height:90px;display:flex}
.quality .tag{width:380px;background:var(--orange);color:var(--white);font-family:"Oswald",Arial,sans-serif;font-size:42px;font-weight:700;line-height:90px;padding-left:24px;clip-path:polygon(0 0,100% 0,92% 50%,100% 100%,0 100%)}
.quality .desc{flex:1;background:var(--orange-soft);color:var(--white);font-size:16px;line-height:1.4;padding:10px 20px;display:flex;align-items:center}

/* evaluate and retain */
.col-title{font-family:"Oswald",Arial,sans-serif;font-size:34px;line-height:40px;text-align:center;color:var(--ink);font-weight:700}
.evaluate{top:1950px;left:90px;width:470px}
.retain{top:1950px;left:620px;width:490px}
.list{list-style:none;margin-top:18px}
.list li{position:relative;padding-left:38px;font-size:17px;line-height:1.4;margin-bottom:12px}
.list li::before{content:"";position:absolute;left:6px;top:5px;width:17px;height:17px;border-radius:50%;border:3px solid var(--orange)}
.note{background:var(--white);padding:12px 16px;font-size:15px;line-height:1.4;margin-top:16px}
.sub{list-style:none;margin:6px 0 0 4px}
.sub li{font-size:14px;padding-left:22px;margin-bottom:3px}
.sub li::before{width:10px;height:10px;top:6px;left:4px;border:2px solid var(--teal)}

/* what else */
.whatelse{top:2710px;left:0;width:1200px}
.whatelse h2{font-size:48px;line-height:56px}
.whatelse .lede{text-align:center;font-size:16px;margin-top:4px}
.attr{top:2800px;width:330px;text-align:center}
.attr .bar{background:var(--teal);color:var(--white);font-family:"Oswald",Arial,sans-serif;font-size:28px;height:48px;line-height:48px;font-weight:700}
.attr.values .bar{background:var(--orange)}
.attr p{font-size:15px;line-height:1.45;margin-top:14px;padding:0 12px}
.attr ol{text-align:left;font-size:13px;line-height:1.35;margin:8px 6px 0 34px}
.attr ol li{margin-bottom:3px}

/* bad hire */
.badhire-title{top:3190px;left:90px;width:660px;text-align:left;font-size:62px;line-height:70px;color:var(--orange)}
.badhire-intro{top:3270px;left:90px;width:620px;font-size:16px;line-height:1.45}
.stats-title{top:3400px;left:0;width:1200px;font-size:30px;line-height:38px;color:var(--orange);font-weight:500}
.stats{top:3455px;left:90px;width:1020px;list-style:none}
.stats li{position:relative;padding-left:46px;font-size:17px;line-height:1.4;margin-bottom:14px}
.stats li::before{content:"";position:absolute;left:6px;top:3px;width:19px;height:19px;border-radius:50%;border:3px solid var(--orange)}

/* since band */
.since{top:3785px;left:0;width:1200px;height:200px;background:var(--teal-light)}
.since .year{position:absolute;left:60px;top:10px;font-family:"Oswald",Arial,sans-serif;font-size:170px;line-height:180px;color:var(--teal);opacity:.6}
.since p{position:absolute;left:470px;top:28px;width:680px;font-size:17px;line-height:1.5;color:var(--white)}

/* connect */
.connect{top:3985px;left:0;width:1200px;height:334px;background:var(--teal-dark);color:var(--white)}
.connect h2{position:absolute;left:60px;top:18px;font-family:"Oswald",Arial,sans-serif;font-size:34px;line-height:40px;font-weight:700;text-transform:uppercase}
.screen{position:absolute;left:60px;top:120px;width:220px;height:170px;background:linear-gradient(#dfe8e8,#aac6c6)}
.contacts{position:absolute;left:310px;top:118px;list-style:none}
.contacts li{display:flex;align-items:center;font-size:21px;line-height:30px;margin-bottom:14px}
.contacts i{width:32px;height:32px;border-radius:50%;background:var(--white);margin-right:16px;display:flex;align-items:center;justify-content:center;flex:none}
.quote{position:absolute;left:830px;top:96px;width:320px;font-family:"Oswald",Arial,sans-serif;font-size:24px;line-height:28px;text-transform:uppercase;color:var(--cream)}
.quote small{display:block;font-family:"Open Sans",Arial,sans-serif;font-size:13px;line-height:18px;margin-top:4px;text-transform:none}
.brand{position:absolute;left:830px;bottom:18px;display:flex;align-items:center;font-family:"Oswald",Arial,sans-serif;font-size:26px;line-height:32px;color:var(--white)}
.brand::before{content:"";width:26px;height:26px;background:var(--orange);margin-right:12px}
</style>
</head>
<body>

<header class="abs masthead">
  <h1>HIRING THE RIGHT PEOPLE</h1>
  <h2>WHY POTENTIAL TRUMPS EVERYTHING ELSE</h2>
</header>

<div class="abs team-figures" role="img" aria-label="Silhouettes of a group of business people standing together"></div>
<section class="abs intro">
  <p>According to global leadership expert Elena Varga-Moreno, potential now trumps experience and competencies when evaluating employees. It's the number one predictor of success at all levels in every size organization.</p>
  <p>The hallmarks of potential include the ability to adapt and grow. Because companies operate in an increasingly volatile and complex world, they need employees who can easily transition to an ever-changing business environment and grow into challenging new roles. Employees must be able to succeed today and tomorrow, regardless of how much things change.</p>
  <p>That's why you can't use a competency-only based evaluation system when hiring. It's not impossible to predict the qualifications needed to succeed down the road. Hiring right means identifying candidates with the greatest potential and helping them flourish once they're on your team.</p>
</section>

<h2 class="abs heading forces-title">THREE FORCES CONTRIBUTING TO<br>SENIOR TALENT SCARCITY</h2>

<div class="abs force" style="left:90px">
  <div class="pin"><span>1</span></div>
  <svg class="pin-tip" width="40" height="22" viewBox="0 0 40 22"><path d="M0 0h40L20 22z" fill="#9a9a9a"/></svg>
  <div class="force-box"><h3>GLOBALIZATION</h3><p>With the pace of globalization charging full steam ahead, companies in developed and developing nations must compete for talent like never before. For example, the International Monetary Fund predicts 70% of the world's growth by 2016 will come from emerging markets.</p></div>
</div>
<div class="abs force" style="left:450px">
  <div class="pin"><span>2</span></div>
  <svg class="pin-tip" width="40" height="22" viewBox="0 0 40 22"><path d="M0 0h40L20 22z" fill="#9a9a9a"/></svg>
  <div class="force-box"><h3>DEMOGRAPHICS</h3><p>The percentage of senior executives in the sought-after 35 to 44-year-old age group has been dwindling. During the past decade, this demographic shift primarily affected the U.S. and Europe. However, by 2020, Russia, Canada, South Korea and China will have more workers entering retirement than the workforce.</p></div>
</div>
<div class="abs force" style="left:810px">
  <div class="pin"><span>3</span></div>
  <svg class="pin-tip" width="40" height="22" viewBox="0 0 40 22"><path d="M0 0h40L20 22z" fill="#9a9a9a"/></svg>
  <div class="force-box"><h3>PIPELINES</h3><p>Companies remain unsure where they will find the next generation of leaders. According to a Northgate Advisory 2014 survey of CEOs in 68 countries, 63% of respondents said they were concerned about the future availability of key skills at all levels. In a Harbor Strategy Partners study, 56% of executives expect critical gaps in their ability to fill senior management roles in coming years.</p></div>
</div>

<h2 class="abs heading qualities-title">IDENTIFYING EMPLOYEE POTENTIAL <b>| THE FIVE CRITICAL QUALITIES</b></h2>

<div class="abs quality" style="top:1310px"><div class="tag">MOTIVATION</div><div class="desc">A powerful commitment to pursue unselfish goals. Highly ambitious with a strong desire to excel. Seeks big, collective goals and shows profound personal humility.</div></div>
<div class="abs quality" style="top:1425px"><div class="tag">CURIOSITY</div><div class="desc">Pursues new experiences, knowledge and candid feedback. Remains open to learning and change.</div></div>
<div class="abs quality" style="top:1540px"><div class="tag">INSIGHT</div><div class="desc">Gathers and makes sense of information that might lead to new possibilities. Sees connections where others don't.</div></div>
<div class="abs quality" style="top:1655px"><div class="tag">ENGAGEMENT</div><div class="desc">Uses emotion and logic to communicate a persuasive vision. Connects with work and people.</div></div>
<div class="abs quality" style="top:1770px"><div class="tag">DETERMINATION</div><div class="desc">Fights for difficult goals despite challenges and bounces back from adversity.</div></div>

<section class="abs evaluate">
  <h3 class="col-title">HOW TO<br>EVALUATE POTENTIAL</h3>
  <div class="note">To determine if a candidate believes in self-improvement, enjoys learning and can recover from missteps, you need to uncover concrete examples by:</div>
  <ul class="list">
    <li>Digging into personal and professional histories</li>
    <li>Conducting in-depth interviews</li>
    <li>Thoroughly checking references</li>
    <li>Asking pointed questions, such as:
      <ul class="list sub">
        <li>How do you react when someone challenges you?</li>
        <li>How do you invite input from others on your team?</li>
        <li>What do you do to broaden your thinking, experience or personal growth?</li>
        <li>How do you foster learning in your organization?</li>
        <li>What steps do you take to seek out the unknown?</li>
      </ul>
    </li>
  </ul>
</section>

<section class="abs retain">
  <h3 class="col-title">HOW TO RETAIN<br>HIGH-POTENTIAL TALENT</h3>
  <ul class="list">
    <li>Offer development opportunities that push employees out of their comfort zones, but don't stretch them beyond their limits.</li>
    <li>Create autonomy in the four "T" dimensions:
      <ul class="list sub">
        <li>Task (what they do)</li>
        <li>Time (when they do it)</li>
        <li>Team (whom they do it with)</li>
        <li>Technique (how they do it)</li>
      </ul>
    </li>
    <li>Design an environment in which employees can master their skills and excel. Help them by setting difficult, yet attainable, challenges and eliminating distractions.</li>
    <li>Establish a purpose in all work so employees know they're serving something bigger than themselves. Engage them in a greater team, organizational or societal goal.</li>
    <li>Compensate high-potential employees to reflect their contribution and effort.</li>
  </ul>
</section>

<section class="abs whatelse">
  <h2 class="heading">WHAT ELSE DO YOU LOOK FOR?</h2>
  <p class="lede">Potential is the defining measurement of executives today. However, you should still integrate other evaluation criteria into the hiring decision:</p>
</section>
<div class="abs attr" style="left:90px"><div class="bar">INTELLIGENCE</div><p>Assess a candidate's general intelligence, including analytical, verbal, mathematical and logical reasoning, by considering educational background, job experience and interview responses.</p></div>
<div class="abs attr values" style="left:435px"><div class="bar">VALUES</div><p>Use interviews and reference checks to gauge honesty, integrity and whether the candidate shares your organization's core values.</p></div>
<div class="abs attr" style="left:780px"><div class="bar">LEADERSHIP ABILITIES</div><p>Although position and organization requirements will vary, the very best leaders tend to have some measure of these eight abilities:</p>
  <ol>
    <li>Strategic Orientation – engaging in complex analytical thinking</li>
    <li>Market Insight – understanding how the market affects the business</li>
    <li>Results Orientation – committing to improve business results</li>
    <li>Customer Impact – passionately serving the customer</li>
    <li>Collaboration and Influence – working with peers outside the chain of command</li>
    <li>Organizational Development – developing talent to improve the company</li>
    <li>Team Leadership – focusing and aligning teams</li>
    <li>Change Leadership – transforming an organization toward a new goal</li>
  </ol>
</div>

<h2 class="abs heading badhire-title">THE CO$T OF A BAD HIRE</h2>
<p class="abs badhire-intro">When you make a bad hiring decision, the cost to the organization can be staggering. Not only will the business lose the money it sank into sourcing, recruiting and hiring, but the loss in productivity will ripple throughout the company.</p>
<h3 class="abs heading stats-title">SOME EYE-OPENING STATS INCLUDE:</h3>
<ul class="abs stats">
  <li>The U.S. Department of Labor and Statistics determined the average cost of a bad hiring decision can equal 30% of the employee's first-year salary.</li>
  <li>According to PeopleDesk Weekly, it costs $7,000 to replace salaried employees, $10,000 to replace a mid-level employee, and $40,000 to replace a senior executive.</li>
  <li>A Talent Practice Review study found as much as 80% of employee turnover can be attributed to bad hiring decisions.</li>
  <li>In a 2012 Civic Workplace Research Council survey, 66% of employers said they experienced negative effects of bad hires, with 37% of this number affecting employee morale, 18% impacting client relationships and 10% causing a decrease in sales.</li>
</ul>

<section class="abs since">
  <div class="year">1994</div>
  <p>Serving businesses since 1994, MERIDIAN STAFFING GROUP offers a full spectrum of workforce solutions, including talent sourcing, temporary staffing solutions, executive recruitment and behavioral assessment consulting and coaching. Matching the highest caliber candidates to fit specific corporate cultures, client companies experience a 94% retention rate of placed candidates.</p>
</section>

<section class="abs connect">
  <h2>CONNECT WITH MERIDIAN<br>STAFFING GROUP TODAY</h2>
  <div class="screen" role="img" aria-label="Laptop showing the company website"></div>
  <ul class="contacts">
    <li><i><svg width="18" height="18" viewBox="0 0 24 24"><path d="M6.6 10.8a15 15 0 0 0 6.6 6.6l2.2-2.2a1 1 0 0 1 1-.25 11 11 0 0 0 3.6.6 1 1 0 0 1 1 1V20a1 1 0 0 1-1 1A17 17 0 0 1 3 4a1 1 0 0 1 1-1h3.5a1 1 0 0 1 1 1 11 11 0 0 0 .6 3.6 1 1 0 0 1-.25 1z" fill="#2f6f70"/></svg></i>555-014-2200</li>
    <li><i></i>www.meridianstaffing.example</li>
    <li><i></i>@meridianjobs</li>
    <li><i></i>social.example/meridianstaffing</li>
  </ul>
  <div class="quote">"It's not the how or the what but the who: succeed by surrounding yourself with the best."<small>— Elena Varga-Moreno</small></div>
  <div class="brand">Meridian Staffing Group</div>
</section>

</body>
</html>
```